Yoga Teacher needs a Flyer for her Yin Yoga Teacher Training

I need a 4 x 6 postcard design for an in-person teacher training I'm offering in Doylestown, PA this summer. It needs to be full color both sides and I'll attach the printing and design specs below. My current logo is Nora Pelham logo in a pink script, which should be included somewhere. The biggest text should be "Yin Yoga Teacher Training" with the following smaller text somewhere on either the front or the back. August 4 - 8 at Bluewren Yoga Studio 287 Larch Avenue, Doylestown PA. For more details visit www.norapelhamyoga.example. And then if there's space on the back, please include this text: Discover the amazing benefits of yin yoga and somatic meditation in this 5-day in-person only immersion for both teachers and experienced students of yoga. Whether you’re interested in teaching or not, this weeklong course will deepen your yoga practice and change your life. You’ll learn 25 yin yoga postures and 5 somatic meditation techniques - all of which are incredible for pain relief and reducing tension. Not only will you be guided through the practice of these techniques, you’ll also participate in a vibrant discourse between teacher and student so you understand the why and the how behind what you’re learning. Nora Pelham has been leading yin yoga teacher trainings for the past 15 years and brings a wealth of information to the classroom. She’s also an expert at creating relaxed in-person learning environments where everyone feels safe to be themselves.
I've attached a bunch of different pictures that you can use. There should be one picture of me with my full body and one headshot. You can decide which picture goes on the front and which on the back - and feel free to crop or adjust any of the photos. I've also attached the color palette and font style guide for my brand. Reach out with any questions! Thank you!
Look and feel
Each slider illustrates characteristics of the customer's brand and the style your logo design should communicate.

```html
<!DOCTYPE html>
<html lang="en">
<head>
<meta charset="utf-8">
<title>Yin Yoga Teacher Training – Postcard</title>
<link rel="stylesheet" href="https://fonts.googleapis.com/css2?family=Poppins:wght@600;700&display=swap">
<style>
  :root {
    --page: #4a4b4d;
    --card: #ffffff;
    --teal: #3f7272;
    --plum: #5a3460;
    --ink: #1c1c1c;
    --blush: #f6c6d3;
    --blush-soft: #fbe3ea;
    --rose: #e7a9bd;
    --lilac: #a874b8;
    --skin: #e3b9a4;
  }
  * { box-sizing: border-box; margin: 0; padding: 0; }
  html, body {
    width: 1200px; height: 887px; overflow: hidden;
    background: var(--page);
    font-family: "Poppins", sans-serif;
  }
  .postcard {
    position: absolute; left: 0; top: 43px;
    width: 1200px; height: 800px;
    background: var(--card);
    overflow: hidden;
  }
  .wash {
    position: absolute; left: 30px; top: 0; width: 840px; height: 800px;
    background:
      radial-gradient(ellipse 46% 42% at 38% 48%, var(--blush) 0%, rgba(246,198,211,0.7) 55%, rgba(246,198,211,0) 100%),
      radial-gradient(ellipse 40% 40% at 70% 30%, var(--blush) 0%, rgba(246,198,211,0) 100%),
      radial-gradient(ellipse 35% 30% at 55% 85%, var(--blush-soft) 0%, rgba(251,227,234,0) 100%);
  }
  .photo-portrait {
    position: absolute; left: 420px; top: 0; width: 430px; height: 500px;
    border-radius: 48% 48% 30% 30%;
    background: radial-gradient(ellipse at 50% 40%, rgba(240,170,190,0.75), rgba(246,198,211,0) 70%);
  }
  .photo-seated {
    position: absolute; left: 50px; top: 40px; width: 530px; height: 640px;
    border-radius: 40% 40% 22% 22%;
    background: linear-gradient(180deg, rgba(227,185,164,0.85) 0%, rgba(168,116,184,0.85) 45%, rgba(230,236,244,0.95) 75%, rgba(227,185,164,0.6) 100%);
  }
  .brand-mark {
    position: absolute; left: 930px; top: 150px; width: 230px;
    display: flex; align-items: center; gap: 10px;
    font-weight: 600; font-size: 30px; color: var(--plum);
  }
  .brand-mark .dot { width: 14px; height: 14px; border-radius: 50%; background: var(--plum); flex: none; }
  .headline {
    position: absolute; left: 670px; top: 288px;
    font-weight: 700; font-size: 118px; line-height: 1; letter-spacing: -3px;
    color: var(--teal);
  }
  .subhead {
    position: absolute; left: 682px; top: 418px;
    font-weight: 700; font-size: 58px; line-height: 0.95; letter-spacing: -0.5px;
    color: var(--plum); text-transform: uppercase;
  }
  .details {
    position: absolute; left: 690px; top: 552px;
    font-weight: 600; font-size: 21px; line-height: 27px; color: var(--ink);
  }
  .more {
    position: absolute; left: 690px; top: 660px;
    font-weight: 600; font-size: 21px; color: var(--ink);
  }
  .web-pill {
    position: absolute; left: 684px; top: 694px;
    padding: 4px 18px 5px;
    border-radius: 20px; background: var(--teal);
    font-weight: 600; font-size: 22px; color: #ffffff;
  }
  .signature {
    position: absolute; left: 60px; top: 680px;
    font-weight: 600; font-size: 46px; color: var(--rose);
    letter-spacing: 1px;
  }
</style>
</head>
<body>
  <main class="postcard">
    <div class="wash" aria-hidden="true"></div>
    <div class="photo-portrait" role="img" aria-label="Faint pink-toned headshot of the teacher with hands in prayer position"></div>
    <div class="photo-seated" role="img" aria-label="Full-body photo of the teacher seated in a twist pose, wearing a purple top and white leggings"></div>

    <div class="brand-mark"><span class="dot"></span><span>bluewren yoga</span></div>

    <h1 class="headline">Yin Yoga</h1>
    <h2 class="subhead">Teacher<br>Training</h2>

    <p class="details">August 4 - 8<br>at Bluewren Yoga Studio<br>287 Larch Avenue, Doylestown PA.</p>
    <p class="more">For more details visit</p>
    <p class="web-pill">www.norapelhamyoga.example</p>

    <p class="signature">Nora Pelham Yoga</p>
  </main>
</body>
</html>
```